Business Card for Dental Office

Our office is in the Hillcrest section of San Diego, California which is a well-established area. Maybe the back can be a map of our office location

```html
<!DOCTYPE html>
<html lang="en">
<head>
<meta charset="utf-8">
<title>Elmgrove Dental – Business Card</title>
<link href="https://fonts.googleapis.com/css2?family=Questrial&family=Montserrat:wght@600;700&display=swap" rel="stylesheet">
<style>
  :root {
    --page-bg: #efefef;
    --card-shadow: rgba(0,0,0,0.18);
    --map-cream: #f4efdc;
    --map-sand: #ece1b8;
    --map-block: #d9d6cc;
    --map-water: #bcd3e6;
    --map-park: #cfe2b5;
    --map-road: #f2c98a;
    --band: #000000;
    --band-text: #ffffff;
    --card-grey: #9d9d9d;
    --ink: #111111;
    --pin: #14304a;
  }
  * { margin: 0; padding: 0; box-sizing: border-box; }
  html, body { width: 1200px; height: 1200px; overflow: hidden; }
  body {
    background: var(--page-bg);
    font-family: "Questrial", "Century Gothic", sans-serif;
    color: var(--ink);
    position: relative;
  }
  .card {
    position: absolute;
    left: 334px;
    width: 531px;
    height: 316px;
    box-shadow: 0 4px 14px var(--card-shadow);
    overflow: hidden;
  }
  .card--front { top: 180px; background: var(--band); }
  .card--back { top: 632px; background: var(--card-grey); }

  .location-map {
    position: absolute; left: 0; top: 0;
    width: 531px; height: 224px;
    background:
      radial-gradient(ellipse 120px 160px at 22% 40%, rgba(188,211,230,0.75), transparent 70%),
      radial-gradient(ellipse 90px 70px at 78% 70%, rgba(207,226,181,0.6), transparent 70%),
      radial-gradient(ellipse 140px 90px at 12% 85%, rgba(242,201,138,0.55), transparent 70%),
      radial-gradient(ellipse 160px 110px at 40% 30%, rgba(217,214,204,0.7), transparent 70%),
      linear-gradient(135deg, var(--map-sand), var(--map-cream) 50%, var(--map-sand));
  }
  .map-marker {
    position: absolute; left: 262px; top: 88px;
    display: flex; align-items: flex-start; gap: 6px;
  }
  .map-marker__label {
    font-family: "Montserrat", sans-serif;
    font-weight: 700; font-size: 17px; line-height: 19px;
    color: var(--ink); text-align: center; margin-top: 2px;
  }
  .hours {
    position: absolute; left: 33px; top: 246px;
    color: var(--band-text);
  }
  .hours__title {
    font-family: "Montserrat", sans-serif; font-weight: 700;
    font-size: 11px; letter-spacing: 6px; margin-bottom: 4px;
  }
  .hours__line { font-size: 13px; line-height: 16px; }

  .brand {
    position: absolute; left: 30px; top: 126px; width: 212px;
    display: flex; align-items: center; gap: 10px;
    font-size: 28px; line-height: 31px; color: var(--ink);
  }
  .brand__dot { width: 18px; height: 18px; border-radius: 50%; background: var(--ink); flex: none; }
  .divider {
    position: absolute; left: 265px; top: 93px;
    width: 3px; height: 133px; background: var(--ink);
  }
  .contact { position: absolute; left: 298px; top: 80px; }
  .contact__name { font-size: 27px; line-height: 30px; }
  .contact__role { font-size: 16px; line-height: 20px; margin-bottom: 4px; }
  .contact__row { display: flex; align-items: flex-start; font-size: 17.5px; line-height: 20.5px; }
  .contact__icon { width: 22px; flex: none; display: flex; justify-content: flex-start; padding-top: 3px; }
</style>
</head>
<body>
  <section class="card card--front">
    <div class="location-map" role="img" aria-label="Street map of the neighbourhood around the dental office, with river, parks and main roads"></div>
    <div class="map-marker">
      <svg width="18" height="28" viewBox="0 0 18 28" aria-hidden="true">
        <path d="M9 0C4 0 0 4 0 9c0 7 9 19 9 19s9-12 9-19c0-5-4-9-9-9z" fill="var(--pin)"/>
        <path d="M9 4.2l1.3 2.8 3 .3-2.3 2 .7 3L9 10.8 6.3 12.3l.7-3-2.3-2 3-.3z" fill="#fff"/>
      </svg>
      <div class="map-marker__label">Elmgrove<br>Dental</div>
    </div>
    <div class="hours">
      <div class="hours__title">HOURS:</div>
      <div class="hours__line">Monday-Thursday: 7:30AM – 5:30PM</div>
      <div class="hours__line">Friday: 7:00AM to 5:00PM</div>
    </div>
  </section>

  <section class="card card--back">
    <div class="brand"><span class="brand__dot"></span><span>Elmgrove Dental</span></div>
    <div class="divider"></div>
    <div class="contact">
      <div class="contact__name">Your Name</div>
      <div class="contact__role">CEO</div>
      <div class="contact__row">
        <span class="contact__icon"><svg width="11" height="15" viewBox="0 0 11 15"><path d="M5.5 0C2.5 0 0 2.4 0 5.4 0 9.5 5.5 15 5.5 15S11 9.5 11 5.4C11 2.4 8.5 0 5.5 0z" fill="var(--ink)"/><circle cx="5.5" cy="5.4" r="2" fill="var(--card-grey)"/></svg></span>
        <span>Full Address, FA 01<br>City Country</span>
      </div>
      <div class="contact__row">
        <span class="contact__icon"><svg width="13" height="13" viewBox="0 0 24 24"><path d="M6.6 10.8c1.4 2.8 3.8 5.1 6.6 6.6l2.2-2.2c.3-.3.7-.4 1-.2 1.1.4 2.3.6 3.6.6.6 0 1 .4 1 1V20c0 .6-.4 1-1 1C10.6 21 3 13.4 3 4c0-.6.4-1 1-1h3.5c.6 0 1 .4 1 1 0 1.3.2 2.5.6 3.6.1.3 0 .7-.2 1l-2.3 2.2z" fill="var(--ink)"/></svg></span>
        <span>0123 456 789</span>
      </div>
      <div class="contact__row">
        <span class="contact__icon"><svg width="13" height="11" viewBox="0 0 13 11"><rect x="0.75" y="0.75" width="11.5" height="9.5" fill="none" stroke="var(--ink)" stroke-width="1.5"/><path d="M1 1l5.5 5 5.5-5" fill="none" stroke="var(--ink)" stroke-width="1.5"/></svg></span>
        <span>info@yourbusiness.com</span>
      </div>
      <div class="contact__row">
        <span class="contact__icon"><svg width="13" height="13" viewBox="0 0 14 14"><circle cx="7" cy="7" r="6" fill="none" stroke="var(--ink)" stroke-width="1.3"/><ellipse cx="7" cy="7" rx="2.6" ry="6" fill="none" stroke="var(--ink)" stroke-width="1.1"/><path d="M1 7h12" stroke="var(--ink)" stroke-width="1.1"/></svg></span>
        <span>www.yourbusiness.com</span>
      </div>
    </div>
  </section>
</body>
</html>
```